Events By Halvane

Weddings, Corporate, Special Events
Memorable Catering, Personalized Menus, Custom Layout & Designs
Professional Staff, Excellent Service
Our Mission is Turning YOUR Vision into a Reality

Odette Halvane, Principal Planner
ph. 202 418-7352 - fax 301-847-2951
Email - eventsbyhalvane@mailtrove.com
Web - www.cateringbyhalvane.com
cateringbyhalvane@Instagram

Target Market(s)

All Brides, Corprate Business, Special Events

Industry/Entity Type

Hospitality

Contact Information for Business Card

clean but affective

Font styles to use
Serif
Sans Serif
Script

Colors

Designer to choose colors to be used in the design.

Requirements
Must have
• logo with tagline using colors that will enhance what
• some pictures of nice table scape, hors d'oevures, upscale foods......
Nice to have
• Event: Something that happens or is regarded as happening, an occurrence especially one of some importance.
Should not have
• Use Logo on both sides

```html
<!DOCTYPE html>
<html lang="en">
<head>
<meta charset="utf-8">
<title>Events By Halvane – Business Card</title>
<link rel="stylesheet" href="https://fonts.googleapis.com/css2?family=Libre+Baskerville:wght@400;700&display=swap">
<style>
  :root {
    --stage: #2b2b2c;
    --card-top: #423c3b;
    --card-bottom: #2f2a29;
    --teal: #1fa9b4;
    --ink: #f1eeec;
    --muted: #a7a19f;
    --rule: #8a8583;
  }
  * { box-sizing: border-box; margin: 0; padding: 0; }
  html, body { width: 1200px; height: 1200px; overflow: hidden; }
  body {
    background: var(--stage);
    font-family: "Libre Baskerville", Georgia, serif;
    color: var(--ink);
    position: relative;
  }
  .card {
    position: absolute;
    left: 140px;
    width: 920px;
    height: 520px;
    border-radius: 36px;
    background: radial-gradient(ellipse at 45% 25%, var(--card-top), var(--card-bottom) 75%);
    box-shadow: 0 18px 40px rgba(0,0,0,.45);
  }
  .card--services { top: 50px; }
  .card--contact { top: 630px; }

  .brand {
    position: absolute;
    display: flex;
    align-items: center;
    justify-content: center;
    gap: 14px;
  }
  .brand__mark {
    width: 18px; height: 18px; border-radius: 50%;
    background: var(--ink); flex: none;
  }
  .brand__name {
    font-weight: 400;
    color: var(--ink);
    white-space: nowrap;
  }
  .card--services .brand { left: 0; right: 0; top: 130px; }
  .card--services .brand__name { font-size: 26px; }
  .card--contact .brand { left: 20px; width: 430px; top: 240px; }
  .card--contact .brand__name { font-size: 26px; }

  .service-list { position: absolute; list-style: none; }
  .service-list li {
    display: flex; align-items: center; gap: 14px;
    font-size: 19px; height: 36px; white-space: nowrap;
  }
  .service-list--left { left: 70px; top: 225px; }
  .service-list--right { right: 60px; top: 255px; }
  .service-list--right li { justify-content: flex-end; }

  .icon { width: 30px; height: 30px; flex: none; }
  .icon circle.badge { fill: var(--teal); }
  .icon .glyph { fill: none; stroke: #fff; stroke-width: 1.8; stroke-linecap: round; stroke-linejoin: round; }
  .icon .glyph-fill { fill: #fff; }

  .mission {
    position: absolute; left: 0; right: 0; bottom: 42px;
    text-align: center; color: var(--teal);
    font-weight: 700; font-size: 20px; letter-spacing: .5px;
  }

  .divider {
    position: absolute; left: 470px; top: 100px;
    width: 3px; height: 300px; background: var(--rule);
  }
  .person { position: absolute; left: 520px; top: 95px; }
  .person__name { font-size: 38px; font-weight: 700; color: var(--teal); letter-spacing: 1px; }
  .person__title { font-size: 20px; margin-top: 4px; }
  .contact-list { list-style: none; margin-top: 26px; }
  .contact-list li {
    display: flex; align-items: center; gap: 14px;
    font-size: 19px; height: 44px; white-space: nowrap;
  }
  .contact-list .icon { width: 34px; height: 34px; }
</style>
</head>
<body>

<section class="card card--services" aria-label="Card back: services">
  <div class="brand">
    <span class="brand__mark"></span>
    <span class="brand__name">Events By Halvane</span>
  </div>

  <ul class="service-list service-list--left">
    <li><svg class="icon" viewBox="0 0 30 30"><circle class="badge" cx="15" cy="15" r="15"/><circle class="glyph" cx="12" cy="16" r="5"/><circle class="glyph" cx="18" cy="16" r="5"/></svg>Weddings</li>
    <li><svg class="icon" viewBox="0 0 30 30"><circle class="badge" cx="15" cy="15" r="15"/><circle class="glyph-fill" cx="15" cy="11" r="4"/><path class="glyph-fill" d="M8 22c0-5 14-5 14 0z"/></svg>Corporate</li>
    <li><svg class="icon" viewBox="0 0 30 30"><circle class="badge" cx="15" cy="15" r="15"/><rect class="glyph" x="8" y="9" width="14" height="12" rx="1.5"/><path class="glyph" d="M8 13h14M11 7v4M19 7v4"/></svg>Special Events</li>
    <li><svg class="icon" viewBox="0 0 30 30"><circle class="badge" cx="15" cy="15" r="15"/><path class="glyph-fill" d="M8 19a7 7 0 0 1 14 0z"/><path class="glyph" d="M7 21h16"/></svg>Memorable Catering</li>
  </ul>

  <ul class="service-list service-list--right">
    <li>Personalized Menus<svg class="icon" viewBox="0 0 30 30"><circle class="badge" cx="15" cy="15" r="15"/><path class="glyph" d="M9 11h12M9 15h12M9 19h12"/></svg></li>
    <li>Custom Layout &amp; Designs<svg class="icon" viewBox="0 0 30 30"><circle class="badge" cx="15" cy="15" r="15"/><path class="glyph" d="M15 8a7 7 0 1 0 0 14c2 0 1-3 3-3h2a3 3 0 0 0 2-3 7 7 0 0 0-7-8z"/><circle class="glyph-fill" cx="12" cy="13" r="1.3"/><circle class="glyph-fill" cx="16" cy="12" r="1.3"/></svg></li>
    <li>Professional Staff<svg class="icon" viewBox="0 0 30 30"><circle class="badge" cx="15" cy="15" r="15"/><circle class="glyph-fill" cx="10" cy="12" r="2.5"/><circle class="glyph-fill" cx="15" cy="11" r="2.8"/><circle class="glyph-fill" cx="20" cy="12" r="2.5"/><path class="glyph-fill" d="M7 21c0-4 16-4 16 0z"/></svg></li>
    <li>Excellent Service<svg class="icon" viewBox="0 0 30 30"><circle class="badge" cx="15" cy="15" r="15"/><path class="glyph" d="M9 15l4 4 8-8" stroke-width="2.6"/></svg></li>
  </ul>

  <p class="mission">Our Mission is Turning YOUR Vision into a Reality</p>
</section>

<section class="card card--contact" aria-label="Card front: contact">
  <div class="brand">
    <span class="brand__mark"></span>
    <span class="brand__name">Events By Halvane</span>
  </div>

  <div class="divider"></div>

  <div class="person">
    <div class="person__name">Odette Halvane</div>
    <div class="person__title">Principal Planner</div>
    <ul class="contact-list">
      <li><svg class="icon" viewBox="0 0 30 30"><circle class="badge" cx="15" cy="15" r="15"/><path class="glyph-fill" d="M10 8l3 0 1 4-2 1.5a9 9 0 0 0 4.5 4.5L18 16l4 1v3a2 2 0 0 1-2 2A12 12 0 0 1 8 10a2 2 0 0 1 2-2z"/></svg>202 418-7352</li>
      <li><svg class="icon" viewBox="0 0 30 30"><circle class="badge" cx="15" cy="15" r="15"/><rect class="glyph" x="10" y="7" width="10" height="5"/><rect class="glyph" x="7" y="12" width="16" height="7" rx="1.5"/><rect class="glyph" x="10" y="16" width="10" height="6"/></svg>301-847-2951</li>
      <li><svg class="icon" viewBox="0 0 30 30"><circle class="badge" cx="15" cy="15" r="15"/><rect class="glyph-fill" x="7" y="10" width="16" height="11" rx="1.5"/><path d="M7.5 11l7.5 6 7.5-6" fill="none" stroke="#1fa9b4" stroke-width="1.6"/></svg>eventsbyhalvane@mailtrove.com</li>
      <li><svg class="icon" viewBox="0 0 30 30"><circle class="badge" cx="15" cy="15" r="15"/><circle class="glyph" cx="15" cy="15" r="8"/><path class="glyph" d="M7 15h16M15 7c-4 5-4 11 0 16M15 7c4 5 4 11 0 16"/></svg>www.cateringbyhalvane.com</li>
      <li><svg class="icon" viewBox="0 0 30 30"><circle class="badge" cx="15" cy="15" r="15"/></svg>@cateringbyhalvane</li>
    </ul>
  </div>
</section>

</body>
</html>
```